Social Media Graphics - Copperfield Loop

Create 6-7 individual social media graphics (square size) to encourage folks to join our online course, using either of the text below (only one set of text per graphic:

The Lantern Ridge Method
How to Create a 7-Figure Business From Scratch
Sign Up Today!

Or

The Lantern Ridge Method
Fast-track Your Way to a Multi-Million Business!
Sign Up Today!

For the color scheme of the graphics, use 1 or 2 colors in the color palette attached; or use any colors that look nice with their outfits; AVOID using red, white and blue altogether because it will look like an Independence Day (4th of July) graphic and we don’t want that; make sure the graphics appeal to both men and women

Make sure each graphic contains 1 of the 2 pics attached; and make sure one of the graphics is all TEXT only.

Target Market(s)

men and women looking to make more money

Industry/Entity Type

entrepreneurship

Requirements
Must have
• see the text document attached
Nice to have
• We are open to a nice color design; the color palette colors are not required, especially we don't want red, white and blue used together
Should not have
• AVOID using red, white and blue altogether because it will look like an Independence Day (4th of July) graphic and we dont want that

```html
<!DOCTYPE html>
<html lang="en">
<head>
<meta charset="utf-8">
<title>The Lantern Ridge Method – Social Graphics</title>
<link href="https://fonts.googleapis.com/css2?family=Anton&family=Archivo+Black&family=Oswald:wght@300;500;600&family=Poppins:wght@500;600&display=swap" rel="stylesheet">
<style>
  :root{
    --rust-dark:#9a2916;
    --rust:#c23f27;
    --rust-light:#d4553c;
    --ink:#1d1d1f;
    --paper:#ffffff;
    --stage:#d3d4d6;
    --photo-dark:#2a2f3c;
    --photo-mid:#3d5478;
    --photo-rose:#c94a5d;
  }
  *{margin:0;padding:0;box-sizing:border-box}
  html,body{width:1200px;height:820px;overflow:hidden;background:var(--stage)}
  .board{position:relative;width:1200px;height:820px}
  .tile{position:absolute;width:346px;height:346px;overflow:hidden;background:var(--paper);box-shadow:0 4px 10px rgba(0,0,0,.28)}
  .gradient-rust{background:linear-gradient(90deg,var(--rust-dark),var(--rust-light))}
  .abs{position:absolute}
  .photo{position:absolute;background:linear-gradient(160deg,var(--photo-dark),var(--photo-mid))}
  .anton{font-family:"Anton",sans-serif;line-height:1;text-transform:uppercase;white-space:nowrap}
  .oswald{font-family:"Oswald",sans-serif;line-height:1;white-space:nowrap}
  .archivo{font-family:"Archivo Black",sans-serif;line-height:1;white-space:nowrap}
  .poppins{font-family:"Poppins",sans-serif;line-height:1.2;white-space:nowrap}
  .italic{font-style:italic}
  .center{text-align:center;left:0;right:0}

  .pill{position:absolute;display:flex;align-items:center;border-radius:40px;font-family:"Oswald",sans-serif;font-weight:600;font-style:italic;white-space:nowrap}
  .pill svg{flex:none}
  .pill--dark{background:var(--ink);color:var(--paper)}
  .pill--light{background:var(--paper);color:var(--rust)}

  .t1-head{top:0;left:0;width:346px;height:203px}
  .t1-band{top:300px;left:0;width:346px;height:46px;background:var(--ink)}
  .t2-band{top:100px;left:0;width:346px;height:77px}
  .t3-tab{top:0;left:8px;width:330px;height:44px;border-radius:0 0 14px 14px}
  .t3-band{top:127px;left:0;width:346px;height:63px;background:var(--ink)}
  .dash{position:absolute;left:0;width:346px;height:3px;background:repeating-linear-gradient(90deg,var(--rust) 0 18px,transparent 18px 26px)}
  .t6-right{top:0;left:157px;width:189px;height:346px}
  .stack-line{display:block}
</style>
</head>
<body>
<main class="board">

  <!-- Tile 1: text only -->
  <section class="tile" style="left:56px;top:52px">
    <div class="abs t1-head gradient-rust"></div>
    <div class="abs center anton" style="top:16px;font-size:46px;color:var(--paper)">The Lantern Ridge</div>
    <div class="abs center anton" style="top:68px;font-size:70px;color:var(--paper)">Method</div>
    <div class="abs center oswald" style="top:163px;font-size:28px;font-weight:300;letter-spacing:2px;color:var(--paper)">HOW TO CREATE A</div>
    <div class="abs center anton" style="top:208px;font-size:86px;color:var(--rust)">7 Figure</div>
    <div class="abs t1-band"></div>
    <div class="abs oswald italic" style="top:311px;left:28px;font-size:19px;font-weight:600;color:var(--paper)">Business From Scratch</div>
    <div class="pill pill--light" style="top:309px;left:213px;height:26px;padding:0 10px 0 3px;font-size:13px">
      <svg width="20" height="20" viewBox="0 0 20 20"><circle cx="10" cy="10" r="10" fill="#c23f27"/><path d="M8 5l5 5-5 5" fill="none" stroke="#fff" stroke-width="2.4"/></svg>
      <span style="margin-left:5px">Sign Up Today!</span>
    </div>
  </section>

  <!-- Tile 2 -->
  <section class="tile" style="left:423px;top:52px">
    <div class="abs t2-band gradient-rust"></div>
    <div class="abs center anton italic" style="top:48px;font-size:41px;color:var(--rust)">The Lantern Ridge</div>
    <div class="abs center anton italic" style="top:106px;font-size:60px;color:var(--paper)">Method</div>
    <div class="abs center oswald italic" style="top:192px;font-size:30px;font-weight:600;color:var(--ink)">How to Create a</div>
    <div class="abs center oswald italic" style="top:235px;font-size:22px;font-weight:600;color:var(--ink)">7-Figure Business From Scratch</div>
    <div class="pill pill--dark" style="top:275px;left:70px;height:50px;padding:0 14px 0 5px;font-size:27px">
      <svg width="40" height="40" viewBox="0 0 40 40"><circle cx="20" cy="20" r="20" fill="#fff"/><path d="M16 11l9 9-9 9" fill="none" stroke="#d4553c" stroke-width="4"/></svg>
      <span style="margin-left:8px">Sign Up Today!</span>
    </div>
  </section>

  <!-- Tile 3 -->
  <section class="tile" style="left:791px;top:52px">
    <div class="abs t3-tab gradient-rust"></div>
    <div class="abs center archivo" style="top:11px;font-size:21px;color:var(--paper)">The Lantern Ridge</div>
    <div class="abs center anton" style="top:52px;font-size:66px;color:var(--rust)">Method</div>
    <div class="abs t3-band"></div>
    <div class="dash" style="top:123px"></div>
    <div class="dash" style="top:191px"></div>
    <div class="abs center anton italic" style="top:134px;font-size:48px;color:var(--paper)">Fast Track</div>
    <div class="photo" role="img" aria-label="Photo of the two course hosts standing together" style="left:170px;top:196px;width:176px;height:150px"></div>
    <div class="abs anton" style="top:208px;left:8px;width:156px;text-align:right;font-size:23px;line-height:1.3;color:var(--rust)">
      <span class="stack-line">Your Way To A</span>
      <span class="stack-line">Multi-Million</span>
      <span class="stack-line">Business!</span>
    </div>
    <div class="pill pill--dark" style="top:308px;left:24px;height:28px;padding:0 10px 0 3px;font-size:14px">
      <svg width="22" height="22" viewBox="0 0 22 22"><circle cx="11" cy="11" r="11" fill="#fff"/><path d="M9 6l5 5-5 5" fill="none" stroke="#d4553c" stroke-width="2.4"/></svg>
      <span style="margin-left:5px">Sign Up Today!</span>
    </div>
  </section>

  <!-- Tile 4 -->
  <section class="tile" style="left:56px;top:423px">
    <div class="abs center archivo" style="top:18px;font-size:26px;color:var(--rust)">THE LANTERN RIDGE</div>
    <div class="abs center archivo" style="top:56px;font-size:44px;color:var(--ink)">METHOD</div>
    <div class="photo" role="img" aria-label="Photo of the two course hosts smiling" style="left:70px;top:104px;width:220px;height:242px;background:linear-gradient(100deg,var(--photo-rose) 0 48%,var(--photo-dark) 52%)"></div>
    <div class="abs" style="top:238px;left:10px;width:326px;height:50px;background:var(--paper)"></div>
    <div class="abs center archivo" style="top:243px;font-size:16px;color:var(--rust-light)">HOW TO CREATE A 7-FIGURE</div>
    <div class="abs center archivo" style="top:266px;font-size:16px;color:var(--ink)">BUSINESS FROM SCRATCH</div>
    <div class="pill" style="top:300px;left:95px;height:34px;padding:0 12px 0 0;background:var(--paper);box-shadow:0 2px 6px rgba(0,0,0,.2);font-family:'Archivo Black',sans-serif;font-style:normal;font-weight:400;font-size:11px;color:var(--rust-light)">
      <svg width="34" height="34" viewBox="0 0 34 34"><circle cx="17" cy="17" r="17" fill="#d4553c"/><path d="M14 10l7 7-7 7" fill="none" stroke="#fff" stroke-width="3"/></svg>
      <span style="margin-left:6px">SIGN UP TODAY!</span>
    </div>
  </section>

  <!-- Tile 5 -->
  <section class="tile gradient-rust" style="left:423px;top:423px">
    <div class="abs" style="top:22px;left:22px;width:300px;height:35px;background:var(--paper)"></div>
    <svg class="abs" style="top:57px;left:22px" width="18" height="8" viewBox="0 0 18 8"><path d="M0 0h18L9 8z" fill="#1d1d1f"/></svg>
    <div class="abs poppins" style="top:26px;left:36px;font-size:20px;font-weight:600;letter-spacing:-.5px;color:var(--ink)">The Lantern Ridge Method</div>
    <div class="abs center poppins" style="top:66px;font-size:22px;font-weight:500;letter-spacing:-.6px;color:var(--paper)">Fast-track Your Way to<br>a Multi-Million Business!</div>
    <div class="abs" style="top:140px;left:166px;width:140px;height:140px;border-radius:50%;background:var(--rust-dark);opacity:.5"></div>
    <div class="photo" role="img" aria-label="Photo of the two course hosts in a bright room" style="left:15px;top:132px;width:246px;height:246px;border-radius:50%;border:3px solid var(--paper)"></div>
    <div class="abs" style="top:148px;left:208px;width:116px;height:116px;border-radius:50%;background:var(--paper)"></div>
    <div class="abs archivo" style="top:176px;left:208px;width:116px;text-align:center;font-size:19px;line-height:1.25;color:var(--ink)">SIGN<br>UP<br>NOW</div>
  </section>

  <!-- Tile 6 -->
  <section class="tile" style="left:791px;top:423px">
    <div class="abs t6-right gradient-rust"></div>
    <div class="abs" style="top:20px;left:17px;width:318px;height:47px;background:var(--paper);box-shadow:0 2px 5px rgba(0,0,0,.2)"></div>
    <div class="abs oswald" style="top:28px;left:17px;width:318px;text-align:center;font-size:25px;font-weight:500;letter-spacing:-.3px;color:var(--rust-dark)">THE LANTERN RIDGE METHOD</div>
    <div class="abs anton" style="top:80px;left:36px;font-size:70px;color:var(--rust-dark)">Fast</div>
    <div class="abs anton" style="top:80px;left:153px;font-size:70px;color:var(--paper)">-Track</div>
    <div class="photo" role="img" aria-label="Photo of the two course hosts standing with arms crossed" style="left:0;top:165px;width:182px;height:181px"></div>
    <div class="abs anton" style="top:176px;right:17px;text-align:right;font-size:24px;line-height:1.15;color:var(--paper)">
      <span class="stack-line">Your Way To A</span>
      <span class="stack-line">Multi-Million</span>
      <span class="stack-line" style="font-size:32px">Business!</span>
    </div>
    <svg class="abs" style="top:293px;left:180px" width="166" height="38" viewBox="0 0 166 38"><path d="M0 0H166L156 19L166 38H0Z" fill="#fff"/></svg>
    <div class="abs oswald" style="top:301px;left:188px;font-size:21px;font-weight:500;color:var(--ink)">SIGN UP TODAY!</div>
  </section>

</main>
</body>
</html>
```